Graphic Design Project

A custom graphic explaining our business.

small urban farms are created, we then buy their products and take them to a distribution center, volunteers come and help us pack it into market baskets (make sure the volunteers reflect adults and kids), then those baskets are delivered to a drop off point where individuals come and pick them up.

It needs to be cute, friendly, and fun. Bright colors, maybe green. I am not a designer, so use your artistic judgment.

Target Market(s)

28-35 Family Friendly, global, diverse, socially counscious consumers

Industry/Entity Type

Business

Requirements
Must have
• This is a link for a custom graphic we made for another project.

http://www.brightmeadowpledge.com/wp-content/uploads/2010/09/Picture-46-1024x274.png

The image must fit into a rectangular window like the image shows in the link.
Nice to have
• Just make sure any people you place in the image reflect diversity, ages, races, etc. thanks.

```html
<!DOCTYPE html>
<html lang="en">
<head>
<meta charset="utf-8">
<title>From Urban Farms to Dropoff Point</title>
<link href="https://fonts.googleapis.com/css2?family=Bebas+Neue&display=swap" rel="stylesheet">
<style>
  :root {
    --leaf: #7dc67a;
    --crate: #989898;
    --basket: #4a8bc9;
    --ink: #111111;
    --paper: #ffffff;
  }
  html, body {
    margin: 0;
    padding: 0;
    overflow: hidden;
    background: var(--paper);
  }
  .flow {
    position: relative;
    width: 1200px;
    height: 600px;
    overflow: hidden;
    background: var(--paper);
  }
  .flow-graphic {
    position: absolute;
    inset: 0;
  }
  .volunteers {
    position: absolute;
    left: 705px;
    top: 4px;
    width: 80px;
    height: 128px;
    background: var(--basket);
    border-radius: 30px 30px 6px 6px;
  }
  .stage-label {
    position: absolute;
    top: 438px;
    width: 260px;
    margin: 0;
    text-align: center;
    font-family: "Bebas Neue", "Oswald", sans-serif;
    font-weight: 400;
    color: var(--ink);
    line-height: 0.98;
    text-shadow: 3px 3px 0 var(--leaf);
  }
  .stage-label .line { display: block; font-size: 54px; }
  .stage-label .line--small { font-size: 29px; letter-spacing: 1px; padding-top: 6px; }
  .label-farms { left: 20px; }
  .label-center { left: 320px; }
  .label-packing { left: 620px; }
  .label-dropoff { left: 920px; }
</style>
</head>
<body>
<main class="flow">
  <svg class="flow-graphic" width="1200" height="600" viewBox="0 0 1200 600" aria-hidden="true">
    <defs>
      <marker id="arrowhead" markerUnits="userSpaceOnUse" markerWidth="44" markerHeight="44" refX="14" refY="22" orient="auto">
        <path d="M0 0 L40 22 L0 44 Z" fill="var(--leaf)"/>
      </marker>
      <g id="basket-icon" fill="none" stroke="var(--basket)" stroke-width="6">
        <line x1="-38" y1="-12" x2="38" y2="-12"/>
        <line x1="-34" y1="2" x2="34" y2="2"/>
        <line x1="-30" y1="16" x2="30" y2="16"/>
        <line x1="-22" y1="-20" x2="-22" y2="26"/>
        <line x1="-8" y1="-20" x2="-8" y2="26"/>
        <line x1="6" y1="-20" x2="6" y2="26"/>
        <line x1="20" y1="-20" x2="20" y2="26"/>
        <line x1="0" y1="-36" x2="22" y2="-14"/>
      </g>
    </defs>

    <!-- flow arrows -->
    <g class="arrows" fill="none" stroke="var(--leaf)" stroke-width="22" stroke-linejoin="miter">
      <polyline points="140,112 210,46 390,46 458,112" marker-end="url(#arrowhead)"/>
      <polyline points="578,238 622,196 656,196" marker-end="url(#arrowhead)"/>
      <polyline points="578,284 622,328 656,328" marker-end="url(#arrowhead)"/>
      <polyline points="824,196 866,196 898,232" marker-end="url(#arrowhead)"/>
      <polyline points="824,328 866,328 898,294" marker-end="url(#arrowhead)"/>
      <line x1="992" y1="150" x2="966" y2="104" marker-end="url(#arrowhead)"/>
      <line x1="1049" y1="136" x2="1049" y2="76" marker-end="url(#arrowhead)"/>
      <line x1="1108" y1="150" x2="1134" y2="104" marker-end="url(#arrowhead)"/>
    </g>

    <!-- urban farms -->
    <circle cx="150" cy="265" r="117" fill="none" stroke="var(--leaf)" stroke-width="8"/>
    <g class="wheat" fill="var(--leaf)">
      <rect x="147" y="180" width="5" height="180"/>
      <ellipse cx="150" cy="182" rx="7" ry="14"/>
      <ellipse cx="136" cy="212" rx="9" ry="17" transform="rotate(-35 136 212)"/>
      <ellipse cx="164" cy="212" rx="9" ry="17" transform="rotate(35 164 212)"/>
      <ellipse cx="134" cy="240" rx="10" ry="19" transform="rotate(-40 134 240)"/>
      <ellipse cx="166" cy="240" rx="10" ry="19" transform="rotate(40 166 240)"/>
      <ellipse cx="134" cy="268" rx="10" ry="19" transform="rotate(-42 134 268)"/>
      <ellipse cx="166" cy="268" rx="10" ry="19" transform="rotate(42 166 268)"/>
      <ellipse cx="135" cy="296" rx="10" ry="18" transform="rotate(-45 135 296)"/>
      <ellipse cx="165" cy="296" rx="10" ry="18" transform="rotate(45 165 296)"/>
      <ellipse cx="137" cy="320" rx="8" ry="15" transform="rotate(-48 137 320)"/>
      <ellipse cx="163" cy="320" rx="8" ry="15" transform="rotate(48 163 320)"/>
    </g>

    <!-- distribution center -->
    <circle cx="452" cy="245" r="117" fill="none" stroke="var(--crate)" stroke-width="8"/>
    <g class="crate" fill="var(--crate)">
      <polygon points="452,238 398,212 335,185 390,186 452,222"/>
      <polygon points="452,238 506,212 569,185 514,186 452,222"/>
      <polygon points="396,226 452,200 508,226 452,252"/>
      <polygon points="390,240 448,268 448,350 390,316"/>
      <polygon points="456,268 514,240 514,316 456,350"/>
    </g>

    <!-- volunteer packing -->
    <circle cx="740" cy="200" r="62" fill="none" stroke="var(--basket)" stroke-width="7"/>
    <use href="#basket-icon" x="740" y="202"/>
    <circle cx="740" cy="327" r="62" fill="none" stroke="var(--basket)" stroke-width="7"/>
    <use href="#basket-icon" x="740" y="329"/>

    <!-- dropoff point -->
    <circle cx="1050" cy="255" r="120" fill="none" stroke="var(--basket)" stroke-width="8"/>
    <use href="#basket-icon" x="1050" y="262" transform="translate(1050 262) scale(1.6) translate(-1050 -262)"/>
  </svg>

  <div class="volunteers" role="img" aria-label="Group of volunteers: two adults and a child waving"></div>

  <h2 class="stage-label label-farms"><span class="line">Urban</span><span class="line">Farms</span></h2>
  <h2 class="stage-label label-center"><span class="line line--small">Distribution</span><span class="line">Center</span></h2>
  <h2 class="stage-label label-packing"><span class="line line--small">Volunteer</span><span class="line">Packing</span></h2>
  <h2 class="stage-label label-dropoff"><span class="line line--small">Dropoff</span><span class="line">Point</span></h2>
</main>
</body>
</html>
```